Vorla constructions

We are predominantly a residential home builder based in Melbourne, Victoria Australia. We construct houses, apartments, townhouses, multi-unit developments.

The name of the company is "Vorla Constructions"
My company believes in building unique construction projects mainly residential homes. The target customers are upmarket Melbourne residents/investors.

I want the brand name "Vorla" to be part of the logo. There's no need to put the word construction in the logo at this stage.

I would also like some ideas for a slogan e.g. "Just build it." or "We build quality homes." But I would like something unique and different for a slogan not the same old cliche.

vorlaconstructions-example.com.au
e: mdelton@vorlaconstructions-example.com.au
M: 0417836519
Address: 8/3 Marlow Close Tallowmere VIC 3990

Director:Mr Desmond Kellingworth

```html
<!DOCTYPE html>
<html lang="en">
<head>
<meta charset="utf-8">
<title>Vorla Constructions – Business Card</title>
<link rel="stylesheet" href="https://fonts.googleapis.com/css2?family=Montserrat:wght@300;400;600;700&display=swap">
<style>
  :root {
    --backdrop: #3a3b3d;
    --card: #262627;
    --card-light: #2e2e30;
    --brand-blue: #1eb1e3;
    --white: #ffffff;
    --paper: #f3f5f7;
  }
  * { box-sizing: border-box; margin: 0; padding: 0; }
  html, body {
    width: 1200px; height: 900px; overflow: hidden;
    background: var(--backdrop);
    font-family: "Montserrat", Arial, sans-serif;
  }
  .stage {
    position: relative; width: 1200px; height: 900px;
    display: flex; align-items: center; justify-content: center; gap: 40px;
  }
  .card {
    position: relative; width: 540px; height: 320px; overflow: hidden;
    background: radial-gradient(ellipse at 50% 40%, var(--card-light), var(--card) 70%);
    box-shadow: 0 14px 30px rgba(0,0,0,.45);
  }
  .wordmark { color: var(--brand-blue); font-weight: 600; letter-spacing: .5px; line-height: 1; white-space: nowrap; }

  /* contact side */
  .card--contact { border-bottom: 4px solid var(--brand-blue); }
  .holder { position: absolute; left: 150px; top: 40px; }
  .holder__name { color: var(--white); font-weight: 700; font-size: 14px; }
  .holder__role { color: var(--brand-blue); font-weight: 400; font-size: 10px; margin-top: 3px; }
  .card--contact .wordmark { position: absolute; right: 40px; top: 98px; font-size: 18px; }
  .contact-list { position: absolute; left: 0; top: 146px; list-style: none; }
  .contact-list li { display: flex; align-items: center; height: 24px; margin-bottom: 10px; }
  .contact-list__bar {
    height: 24px; background: var(--brand-blue); color: var(--white);
    font-size: 10.5px; font-weight: 400; line-height: 24px; padding-left: 50px;
    white-space: nowrap; overflow: hidden;
  }
  .contact-list__icon {
    width: 24px; height: 24px; background: var(--white); margin-left: 4px;
    display: flex; align-items: center; justify-content: center;
  }
  .contact-list__icon svg { width: 14px; height: 14px; }

  /* brand side */
  .card--brand { border-top: 4px solid var(--brand-blue); }
  .card--brand .wordmark { position: absolute; left: 0; right: 0; top: 104px; text-align: center; font-size: 36px; }
  .slogan {
    position: absolute; left: 180px; top: 238px; color: var(--white);
    font-weight: 300; font-size: 15px; white-space: nowrap;
  }
  .brand-bands { position: absolute; left: 0; top: 0; width: 540px; height: 320px; }
</style>
</head>
<body>
<main class="stage">
  <section class="card card--contact" aria-label="Business card, contact side">
    <div class="holder">
      <p class="holder__name">Mr Desmond Kellingworth</p>
      <p class="holder__role">Director</p>
    </div>
    <p class="wordmark">Vorla constructions</p>
    <ul class="contact-list">
      <li>
        <span class="contact-list__bar" style="width:250px">0417836519</span>
        <span class="contact-list__icon"><svg viewBox="0 0 16 16"><rect x="4" y="1" width="8" height="14" rx="1.5" fill="none" stroke="var(--brand-blue)" stroke-width="1.6"/><circle cx="8" cy="12.3" r="0.9" fill="var(--brand-blue)"/></svg></span>
      </li>
      <li>
        <span class="contact-list__bar" style="width:310px">mdelton@vorlaconstructions-example.com.au</span>
        <span class="contact-list__icon"><svg viewBox="0 0 16 16"><rect x="1.5" y="3.5" width="13" height="9" fill="none" stroke="var(--brand-blue)" stroke-width="1.5"/><path d="M1.5 3.5 8 9l6.5-5.5" fill="none" stroke="var(--brand-blue)" stroke-width="1.5"/></svg></span>
      </li>
      <li>
        <span class="contact-list__bar" style="width:270px">vorlaconstructions-example.com.au</span>
        <span class="contact-list__icon"><svg viewBox="0 0 16 16"><circle cx="8" cy="8" r="6.3" fill="none" stroke="var(--brand-blue)" stroke-width="1.4"/><ellipse cx="8" cy="8" rx="2.7" ry="6.3" fill="none" stroke="var(--brand-blue)" stroke-width="1.2"/><path d="M1.7 8h12.6" stroke="var(--brand-blue)" stroke-width="1.2"/></svg></span>
      </li>
      <li>
        <span class="contact-list__bar" style="width:260px">8/3 Marlow Close Tallowmere VIC 3990</span>
        <span class="contact-list__icon"><svg viewBox="0 0 16 16"><path d="M8 15s5-5.2 5-8.8A5 5 0 0 0 3 6.2C3 9.8 8 15 8 15z" fill="var(--brand-blue)"/><circle cx="8" cy="6.2" r="1.8" fill="var(--white)"/></svg></span>
      </li>
    </ul>
  </section>

  <section class="card card--brand" aria-label="Business card, brand side">
    <p class="wordmark">Vorla constructions</p>
    <p class="slogan">We build quality homes</p>
    <svg class="brand-bands" viewBox="0 0 540 320" aria-hidden="true">
      <polygon points="0,226 150,238 162,248 0,236" fill="var(--brand-blue)"/>
      <polygon points="0,236 162,248 150,272 0,272" fill="var(--paper)"/>
      <polygon points="362,262 540,276 540,284 354,270" fill="var(--brand-blue)"/>
      <polygon points="354,270 540,284 540,316 330,316" fill="var(--paper)"/>
    </svg>
  </section>
</main>
</body>
</html>
```